Business Cards and Stationary for Dental Office
Brodley Dental
Use same font as used in my logo
R.T. Brodley
D.D.S, P.C.
418 West R. Parkway
Lawson, MO 64062
rtb@brodleydentalcare.test
www.brodleydentalcare.test
We are looking for clean, simple, professional designs. In addition to Business Card Design we would also like to see designs for letterhead and Envelope.

```html
<!DOCTYPE html>
<html lang="en">
<head>
<meta charset="utf-8">
<title>Brodley Dental – Business Card</title>
<link href="https://fonts.googleapis.com/css2?family=Cinzel:wght@400&family=Open+Sans:wght@400;600;700&display=swap" rel="stylesheet">
<style>
  :root {
    --page-bg: #e9e9e7;
    --card-bg: #ffffff;
    --brand-green: #2c9a4a;
    --brand-green-dark: #228540;
    --swoosh-grey: #8a8d8f;
    --ink-dark: #4a4d50;
    --ink-light: #ffffff;
  }
  * { margin: 0; padding: 0; box-sizing: border-box; }
  html, body {
    width: 1200px; height: 914px; overflow: hidden;
    background: var(--page-bg);
  }
  .business-card {
    position: absolute; left: 100px; top: 167px;
    width: 1000px; height: 580px;
    background: var(--card-bg);
    box-shadow: 0 10px 30px rgba(0,0,0,.18);
    overflow: hidden;
  }
  .card-shapes { position: absolute; inset: 0; }
  .holder {
    position: absolute; left: 110px; top: 62px;
    color: var(--ink-light);
    font-family: "Open Sans", sans-serif;
  }
  .holder-name { font-size: 26px; font-weight: 700; letter-spacing: .3px; }
  .holder-title { font-size: 17px; font-weight: 400; margin-top: 2px; letter-spacing: .5px; }
  .contact-list {
    position: absolute; left: 110px; top: 262px;
    list-style: none;
    font-family: "Cinzel", serif; font-size: 16px;
    color: var(--ink-light);
  }
  .contact-item { display: flex; align-items: center; height: 27px; white-space: nowrap; }
  .contact-icon {
    width: 19px; height: 19px; border-radius: 50%;
    background: var(--ink-light);
    display: inline-flex; align-items: center; justify-content: center;
    margin-right: 14px; flex: none;
  }
  .contact-icon svg { width: 12px; height: 12px; fill: var(--brand-green); }
  .contact-item.no-icon { padding-left: 33px; }
  .brand-block {
    position: absolute; left: 580px; top: 260px; width: 380px;
    display: flex; align-items: center; justify-content: center; gap: 16px;
  }
  .brand-mark {
    width: 48px; height: 48px; border-radius: 50%;
    background: var(--brand-green); flex: none;
  }
  .brand-name {
    font-family: "Open Sans", sans-serif; font-weight: 600;
    font-size: 34px; color: var(--ink-dark);
    line-height: 1; white-space: nowrap;
  }
</style>
</head>
<body>
  <div class="business-card">
    <svg class="card-shapes" viewBox="0 0 1000 580" width="1000" height="580">
      <defs>
        <radialGradient id="greenPanel" cx="0.3" cy="0.4" r="0.8">
          <stop offset="0" stop-color="#2c9a4a"/>
          <stop offset="1" stop-color="#228540"/>
        </radialGradient>
      </defs>
      <path class="green-panel" fill="url(#greenPanel)"
        d="M0 0 H620 C600 110 560 190 500 260 C440 330 420 430 440 580 H0 Z"/>
      <path class="grey-swoosh" fill="#8a8d8f"
        d="M640 0 C628 120 590 200 530 265 C470 330 448 430 458 580 H446 C430 430 452 320 512 255 C575 185 610 110 628 0 Z"/>
    </svg>

    <div class="holder">
      <div class="holder-name">R.T. Brodley</div>
      <div class="holder-title">D.D.S, P.C.</div>
    </div>

    <ul class="contact-list">
      <li class="contact-item"><span class="contact-icon"><svg viewBox="0 0 12 12"><path d="M6 1 L11 6 H9.5 V11 H7 V8 H5 V11 H2.5 V6 H1 Z"/></svg></span>418 West R. Parkway</li>
      <li class="contact-item no-icon">Lawson, MO 64062</li>
      <li class="contact-item"><span class="contact-icon"><svg viewBox="0 0 12 12"><path d="M3 1 L5 3.5 L4 5 C4.8 6.6 5.6 7.4 7 8 L8.5 7 L11 9 L9.5 11 C5 10.5 1.5 7 1 2.5 Z"/></svg></span>816.555.0142</li>
      <li class="contact-item"><span class="contact-icon"><svg viewBox="0 0 12 12"><path d="M2 4 H10 V9 H2 Z M3 1 H9 V3.5 H3 Z"/></svg></span>816.555.0198</li>
      <li class="contact-item"><span class="contact-icon"><svg viewBox="0 0 12 12"><path d="M1 3 H11 V9.5 H1 Z M1.5 3.5 L6 7 L10.5 3.5" stroke="#fff" stroke-width=".8"/></svg></span>rtb@brodleydentalcare.test</li>
      <li class="contact-item"><span class="contact-icon"><svg viewBox="0 0 12 12"><circle cx="6" cy="6" r="5"/><path d="M1 6 H11 M6 1 C3.5 4 3.5 8 6 11 M6 1 C8.5 4 8.5 8 6 11" stroke="#fff" stroke-width=".7" fill="none"/></svg></span>www.brodleydentalcare.test</li>
    </ul>

    <div class="brand-block">
      <div class="brand-mark"></div>
      <div class="brand-name">Brodley Dental</div>
    </div>
  </div>
</body>
</html>
```